Need Epic Web Banner for New Site

We need a banner for our web page. We are BrightMorrow.com, think of us as the Fendlow of the highest quality sports nutrition supplements on the web. Our site is under construction, if you visit our site, this banner will go at the very top above the menu bar. We are marketing supplements a different way then most; we are staying away from hulked out guys on steroids & gimmick magic pills/ slogans. We are all about clean quality products with less ingredients.

We are attaching our logo/ symbol & a text we made in AI for a point of reference. Please help us bring our site and vision of BrightMorrow to life!

We are not married to the colors but GREEN is a must!
Updates

Disregard previous message about Rosa's entry. This platform does not allow me to delet comments I post.

Target Market(s)

Heath Consious, Health Seekers, Active Fit People, Gym Rats, Rock Climbers

Industry/Entity Type

Nutrition

Font styles to use
Other font styles liked:
• Semplicita

Colors
33b8a4
00a990
86cfc6

Requirements
Must have
• For text In addition to BrightMorrow.com we'd like "Not all supplements are created equal"

```html
<!DOCTYPE html>
<html lang="en">
<head>
<meta charset="utf-8">
<title>BrightMorrow.com – Home</title>
<link rel="stylesheet" href="https://fonts.googleapis.com/css2?family=Comfortaa:wght@400&family=Roboto:wght@400&family=Oswald:wght@400&display=swap">
<style>
  :root {
    --page-bg: #ffffff;
    --banner-dark: #07130f;
    --teal: #33b8a4;
    --teal-deep: #00a990;
    --teal-soft: #86cfc6;
    --nav-bg: #a8d6a0;
    --nav-text: #222222;
    --card-border: #dddddd;
    --placeholder-bg: #cccccc;
    --placeholder-text: #969696;
    --link-blue: #337ab7;
    --body-text: #333333;
    --review-red: #d9534f;
  }
  * { box-sizing: border-box; margin: 0; padding: 0; }
  html, body {
    width: 1200px; height: 750px; overflow: hidden;
    background: var(--page-bg);
    font-family: "Roboto", "Helvetica Neue", Arial, sans-serif;
    color: var(--body-text);
  }
  .site-banner {
    position: relative;
    height: 103px;
    background:
      radial-gradient(ellipse 200px 95px at 740px 50px, rgba(0,169,144,0.75), transparent 75%),
      radial-gradient(ellipse 130px 85px at 1060px 55px, rgba(51,184,164,0.6), transparent 80%),
      radial-gradient(ellipse 140px 70px at 110px 70px, rgba(0,169,144,0.35), transparent 80%),
      linear-gradient(90deg, var(--banner-dark), #0a2a24 40%, #0d352d 60%, var(--banner-dark));
  }
  .banner-brand {
    position: absolute; left: 258px; top: 16px;
  }
  .brand-mark {
    display: flex; align-items: center; gap: 12px;
    font-family: "Comfortaa", "Quicksand", sans-serif;
    font-size: 38px; color: var(--teal-soft); line-height: 44px;
  }
  .brand-mark .mark-dot {
    width: 32px; height: 32px; border-radius: 50%;
    border: 5px solid var(--teal-soft);
  }
  .banner-tagline {
    margin: 6px 0 0 45px;
    font-family: "Comfortaa", "Quicksand", sans-serif;
    font-size: 15px; line-height: 20px; letter-spacing: 0.5px;
    color: var(--teal);
  }
  .main-nav {
    height: 44px; background: var(--nav-bg);
    display: flex; align-items: center;
    padding-left: 120px;
    font-size: 12px; color: var(--nav-text);
  }
  .main-nav .nav-brand { font-size: 15px; margin-right: 26px; }
  .main-nav .nav-item { margin-right: 25px; display: flex; align-items: center; gap: 3px; }
  .caret { width: 0; height: 0; border-left: 3.5px solid transparent; border-right: 3.5px solid transparent; border-top: 4px solid var(--nav-text); }
  .content { position: relative; }
  .deal-card {
    position: absolute; left: 120px; top: 17px; width: 221px; height: 239px;
    border: 1px solid var(--card-border); border-radius: 3px; overflow: hidden;
  }
  .placeholder {
    background: var(--placeholder-bg); color: var(--placeholder-text);
    font-family: "Oswald", "Arial Narrow", sans-serif;
    display: flex; align-items: center; justify-content: center;
  }
  .deal-card .placeholder { height: 103px; font-size: 19px; }
  .deal-body { padding: 13px 8px 0 8px; }
  .deal-head { display: flex; justify-content: space-between; font-size: 15px; }
  .deal-head .deal-title { color: var(--link-blue); }
  .deal-desc { font-size: 11.5px; line-height: 17px; margin-top: 10px; }
  .deal-foot { display: flex; justify-content: space-between; align-items: center; margin-top: 18px; font-size: 11.5px; }
  .stars { display: flex; gap: 4px; }
  .stars span { width: 7px; height: 8px; border: 1px solid #e3a7a5; }
  .reviews { color: var(--review-red); }
  .hero-carousel {
    position: absolute; left: 366px; top: 17px; width: 716px; height: 268px;
    font-size: 68px;
    background: linear-gradient(90deg, #a9a9a9 0%, #cbcbcb 12%, #cbcbcb 88%, #a9a9a9 100%);
  }
  .carousel-arrow { position: absolute; top: 131px; width: 13px; height: 16px; border: 1px solid #eeeeee; }
  .carousel-arrow.prev { left: 52px; }
  .carousel-arrow.next { right: 52px; }
  .carousel-dots { position: absolute; bottom: 30px; left: 50%; transform: translateX(-50%); display: flex; gap: 4px; }
  .carousel-dots span { width: 10px; height: 10px; border-radius: 50%; border: 1px solid #fff; }
  .carousel-dots span.active { background: #fff; }
  .section-title { position: absolute; left: 366px; top: 305px; font-size: 17px; font-weight: 400; }
  .product-grid { position: absolute; left: 366px; top: 339px; display: flex; gap: 26px; }
  .product-card { width: 221px; height: 200px; border: 1px solid var(--card-border); border-bottom: none; display: flex; justify-content: center; padding-top: 4px; }
  .product-photo { width: 158px; height: 196px; border-radius: 8px 8px 0 0; }
  .photo-blue { background: linear-gradient(180deg, #3aa6e0 0%, #3aa6e0 40%, #e9ecee 42%, #dfe3e6 100%); }
  .photo-white { width: 118px; background: linear-gradient(180deg, #8f8f8f 0%, #b5b5b5 8%, #f1f3f5 12%, #f7f8f9 85%, #2c6fb5 100%); }
  .photo-orange { width: 150px; background: radial-gradient(ellipse at 50% 55%, #ff8a1c, #e25c05 70%), #e25c05; border-top: 10px solid #2b3e9a; }
</style>
</head>
<body>
  <header class="site-banner" role="img" aria-label="Dark banner with teal-toned photo of athletes lifting weights, with the BrightMorrow.com name and tagline">
    <div class="banner-brand">
      <div class="brand-mark"><span class="mark-dot"></span>BrightMorrow.com</div>
      <p class="banner-tagline">Not all supplements are created equal</p>
    </div>
  </header>
  <nav class="main-nav">
    <span class="nav-brand">BrightMorrow</span>
    <span class="nav-item">Products <span class="caret"></span></span>
    <span class="nav-item">About</span>
    <span class="nav-item">Contact</span>
  </nav>
  <main class="content">
    <aside class="deal-card">
      <div class="placeholder">320×150</div>
      <div class="deal-body">
        <div class="deal-head"><span class="deal-title">Deal of the Week!</span><span>$24.99</span></div>
        <p class="deal-desc">This is a short description. Lorem ipsum dolor sit amet, consectetur adipiscing elit.</p>
        <div class="deal-foot">
          <div class="stars"><span></span><span></span><span></span><span></span><span></span></div>
          <span class="reviews">15 reviews</span>
        </div>
      </div>
    </aside>
    <section class="hero-carousel placeholder">
      800×300
      <span class="carousel-arrow prev"></span>
      <span class="carousel-arrow next"></span>
      <div class="carousel-dots"><span class="active"></span><span></span><span></span></div>
    </section>
    <h2 class="section-title">Protein</h2>
    <div class="product-grid">
      <div class="product-card"><div class="product-photo photo-blue" role="img" aria-label="Product photo of a blue and white whey isolate pouch"></div></div>
      <div class="product-card"><div class="product-photo photo-white" role="img" aria-label="Product photo of a white whey isolate protein tub"></div></div>
      <div class="product-card"><div class="product-photo photo-orange" role="img" aria-label="Product photo of an orange whey protein isolate jar"></div></div>
    </div>
  </main>
</body>
</html>
```